Town Planning Consultants require lstationary design

Require a design to be used for our letterhead and report cover page. We have an approved logo.
we have attached our logo, and our temporary letterhead/cover page (SEE Cover) which we currently adapt for both purposes in the interim pending a permanent design. I have also attached an example (example report cover) of a report cover page that I like. perhaps similar with our colour scheme

Target Market(s)

?

Industry/Entity Type

Town

Colors
249fd4
3176b5

Requirements
Must have
• colours to match logo
• the text content in existing letterhead

```html
<!DOCTYPE html>
<html lang="en">
<head>
<meta charset="utf-8">
<title>Norvale Urban – Report Cover &amp; Letterhead</title>
<link rel="stylesheet" href="https://fonts.googleapis.com/css2?family=Montserrat:wght@400;500;600&family=Open+Sans:wght@400;600&display=swap">
<style>
  :root {
    --brand-blue: #23a5da;
    --brand-deep: #3176b5;
    --brand-grey: #979797;
    --text-grey: #7b7b7b;
    --paper: #ffffff;
    --backdrop: #e9eaec;
  }
  * { box-sizing: border-box; margin: 0; padding: 0; }
  html, body { width: 1200px; height: 921px; overflow: hidden; background: var(--backdrop); }
  .stage { position: relative; width: 1200px; height: 921px; }
  .sheet {
    position: absolute; top: 114px; width: 537px; height: 694px;
    background: var(--paper); overflow: hidden;
    box-shadow: 6px 8px 14px rgba(0,0,0,.22);
  }
  .sheet--cover { left: 42px; }
  .sheet--letter { left: 620px; }

  .brand-name {
    position: absolute; left: 0; right: 0; text-align: center;
    font-family: "Montserrat", sans-serif; font-weight: 500;
    color: var(--brand-blue); letter-spacing: -1px; white-space: nowrap;
  }
  .brand-mark {
    display: inline-block; background: var(--brand-blue);
    vertical-align: middle; margin-right: 12px;
  }
  .sheet--cover .brand-name { top: 70px; font-size: 54px; line-height: 60px; }
  .sheet--cover .brand-mark { width: 34px; height: 34px; }

  .doc-type {
    position: absolute; top: 170px; left: 0; right: 0; text-align: center;
    font-family: "Montserrat", sans-serif; font-weight: 500; font-size: 16px;
    letter-spacing: .5px; color: var(--brand-blue);
  }
  .cover-art { position: absolute; inset: 0; }
  .doc-title {
    position: absolute; top: 211px; left: 0; right: 0; text-align: center;
    font-family: "Montserrat", sans-serif; font-weight: 500; font-size: 24px;
    line-height: 30px; color: #fff;
  }
  .council {
    position: absolute; top: 291px; left: 0; right: 0; text-align: center;
    font-family: "Montserrat", sans-serif; font-weight: 400; font-size: 29px;
    color: var(--brand-blue);
  }
  .site-address {
    position: absolute; top: 421px; left: 10px; right: 10px; text-align: center;
    font-family: "Open Sans", sans-serif; font-weight: 600; color: #fff;
    font-size: 12.5px; line-height: 17px;
  }
  .site-address small { font-size: 11px; }
  .proposal {
    position: absolute; top: 543px; left: 10px; right: 10px; text-align: center;
    font-family: "Montserrat", sans-serif; font-size: 11.5px; color: #fff;
  }
  .issue-date {
    position: absolute; top: 646px; left: 225px; width: 87px; height: 23px;
    border: 1px solid #fff; text-align: center; line-height: 21px;
    font-family: "Montserrat", sans-serif; font-size: 10px; color: #fff;
  }
  .issue-date sup { font-size: 6px; }

  .sheet--letter .brand-name { top: 58px; font-size: 50px; line-height: 56px; }
  .sheet--letter .brand-mark { width: 30px; height: 30px; }
  .rule { position: absolute; height: 1px; background: var(--brand-blue); }
  .rule--head-left { top: 110px; left: 0; width: 150px; }
  .rule--head-right { top: 110px; right: 0; width: 150px; }
  .rule--foot { top: 616px; left: 18px; right: 18px; }

  .contact-list {
    position: absolute; top: 624px; left: 20px; list-style: none;
    font-family: "Montserrat", sans-serif; font-size: 11.5px; line-height: 14px;
    color: var(--text-grey);
  }
  .contact-list li { display: flex; align-items: center; gap: 6px; }
  .contact-list svg { width: 9px; height: 9px; fill: var(--brand-deep); }
  .postal {
    position: absolute; top: 652px; right: 18px; text-align: right;
    font-family: "Montserrat", sans-serif; font-size: 11.5px; line-height: 14px;
    color: var(--text-grey); font-style: normal;
  }
</style>
</head>
<body>
<main class="stage">

  <section class="sheet sheet--cover" aria-label="Report cover">
    <svg class="cover-art" width="537" height="694" viewBox="0 0 537 694" aria-hidden="true">
      <polygon points="0,313 268,362 537,313 537,694 0,694" fill="var(--brand-grey)"/>
      <polygon points="0,325 268,374 537,325 537,694 0,694" fill="var(--brand-blue)"/>
      <polygon points="81,208 450,208 504,278 24,278" fill="var(--brand-blue)"/>
      <polygon points="85,212 446,212 494,274 34,274" fill="var(--brand-grey)"/>
    </svg>
    <div class="brand-name"><span class="brand-mark"></span>Norvale Urban</div>
    <p class="doc-type">DEVELOPMENT APPLICATION</p>
    <h1 class="doc-title">Statement of<br>Environmental Effects</h1>
    <h2 class="council">Ridgeway Shire Council</h2>
    <p class="site-address">LOT 3 DP 512408 &amp; Lot 9 DP31745 No 512 Station Ridge Road &amp; No 7 Mill Lane<br><small>ASHBURN</small></p>
    <p class="proposal">Redevelopment of an Existing Shopping Centre in 2 Stages for “Shop top Housing”.</p>
    <p class="issue-date">25<sup>TH</sup> JULY, 2016</p>
  </section>

  <section class="sheet sheet--letter" aria-label="Letterhead">
    <div class="brand-name"><span class="brand-mark"></span>Norvale Urban</div>
    <span class="rule rule--head-left"></span>
    <span class="rule rule--head-right"></span>
    <span class="rule rule--foot"></span>
    <ul class="contact-list">
      <li><svg viewBox="0 0 10 10"><path d="M2 0h2l1 3-1.5 1a6 6 0 0 0 2.5 2.5L7 5l3 1v2c0 1-1 2-2 2A8 8 0 0 1 0 2c0-1 1-2 2-2z"/></svg>+330 5550-0142</li>
      <li><svg viewBox="0 0 10 10"><path d="M2 0h6v3H2zM0 4h10v4H8v2H2V8H0zM3 7v2h4V7z"/></svg>+330 5550-0187</li>
      <li><svg viewBox="0 0 10 10"><path d="M0 2h10v6H0zM1 3v.4L5 6l4-2.6V3L5 5.5z"/></svg>info@norvaleurban.com</li>
      <li><svg viewBox="0 0 10 10"><path d="M5 0a5 5 0 1 0 0 10A5 5 0 0 0 5 0zm0 1c.6.6 1 1.7 1.2 3.5H3.8C4 2.7 4.4 1.6 5 1zM1.1 5.5h1.8c.1 1.4.4 2.5.9 3.2A4 4 0 0 1 1.1 5.5zm0-1a4 4 0 0 1 2.7-3.2c-.5.7-.8 1.8-.9 3.2zm2.7 1h2.4C6 7.3 5.6 8.4 5 9c-.6-.6-1-1.7-1.2-3.5zm3.3 0h1.8a4 4 0 0 1-2.7 3.2c.5-.7.8-1.8.9-3.2zm0-1c-.1-1.4-.4-2.5-.9-3.2a4 4 0 0 1 2.7 3.2z"/></svg>www.norvaleurban.com</li>
    </ul>
    <address class="postal">742 N, Linden Ave.,<br>Fairhaven, WA 99000</address>
  </section>

</main>
</body>
</html>
```